Business card design for a dynamic IT consulting company

We need a business card design for a young firm, specialized in the Telecommunications/Consulting industry. The name of the company is Brask and Partners Business Consulting Ltd. (Short name: Brask and Partnes)
Brask = solve read reverse, so we aim to be uncomplicated and solution-oriented. The small pipe in our logo is also related to the word solve. So we need a new business card design, which is simple, eye catching and something non traditional (I would probably prefer a square shaped design rather than a rectangle, but open for suggestions). Attached our logo.

Target Market(s)

Usually our customers are Tier1 Telecoms providers (Q-Linkra, Parnexo, etc) and their executives.

Industry/Entity Type

Business

Contact Information for Business Card

Name: Gergely Halmindo
Email: g.halmindo@braskpartnera.hu
Web: www.braskpartnera.hu
Mobile: +36 30 555 0192
Title: Managing Director

Optional:
Company name: Brask and Partners Ltd.
Address: 1047 Budapest, Ravaszi str. 17/B, Hungary

Font styles to use
Other font styles liked:
• helveticaneue_medium, Prime Regular are used now.

Colors

Designer to choose colors to be used in the design.

Requirements
Must have
• I would like to have a 2 sided design.
Nice to have
• I thought if we make the logo a bit bigger (without the company name), that could go to the back with the company name below. I though, if the pipe in the logo is somehow touchable on the business card, would be nice and unique.

```html
<!DOCTYPE html>
<html lang="en">
<head>
<meta charset="utf-8">
<title>Brask and Partners – Business Card</title>
<link rel="stylesheet" href="https://fonts.googleapis.com/css2?family=Arimo:wght@400;700&display=swap">
<style>
  :root {
    --page-bg: #efeeec;
    --card-white: #f7f7f6;
    --card-grey: #5b5c5e;
    --frame-dark: #5a5a5a;
    --band-grey: #5d5e60;
    --text-dark: #454545;
    --name-blue: #0a8fd8;
    --white: #ffffff;
  }
  * { margin: 0; padding: 0; box-sizing: border-box; }
  html, body {
    width: 1200px; height: 960px; overflow: hidden;
    background: var(--page-bg);
    font-family: "Arimo", Arial, sans-serif;
  }
  .card {
    position: absolute; top: 309px;
    width: 342px; height: 343px;
    box-shadow: 1px 2px 4px rgba(0,0,0,0.25);
  }
  .card-front { left: 235px; background: var(--card-white); }
  .card-back { left: 623px; background: var(--card-grey); }
  .card-frame { position: absolute; inset: 14px; }
  .card-front .card-frame { border: 3px solid var(--frame-dark); }
  .card-back .card-frame { border: 2px solid var(--white); }

  .brand-name {
    position: absolute; left: 0; right: 0;
    text-align: center; font-weight: 400; white-space: nowrap;
  }
  .brand-name .brand-square {
    display: inline-block; width: 10px; height: 10px;
    margin-right: 10px; vertical-align: middle;
    position: relative; top: -2px;
  }
  .card-front .brand-name { top: 46px; font-size: 24px; color: var(--frame-dark); }
  .card-front .brand-square { background: var(--name-blue); }
  .card-back .brand-name { top: 190px; font-size: 28px; color: var(--white); }
  .card-back .brand-square { background: var(--white); }

  .phone {
    position: absolute; top: 105px; left: 0; right: 0;
    text-align: center; font-weight: 700; font-size: 17px; color: var(--text-dark);
  }
  .name-band { position: absolute; left: 15px; top: 128px; }
  .person {
    position: absolute; top: 155px; left: 0; right: 0; text-align: center;
  }
  .person-name { font-weight: 700; font-size: 18px; color: var(--name-blue); line-height: 22px; }
  .person-title { font-size: 15px; color: var(--white); line-height: 21px; }
  .contact {
    position: absolute; top: 223px; left: 0; right: 0;
    text-align: center; font-size: 14px; color: var(--text-dark); line-height: 18px;
  }
  .address { margin-top: 11px; }
</style>
</head>
<body>
  <section class="card card-front">
    <div class="card-frame"></div>
    <div class="brand-name"><span class="brand-square"></span>Brask &amp; Partners</div>
    <div class="phone">+36 30 555 0192</div>
    <svg class="name-band" width="313" height="95" viewBox="0 0 313 95">
      <polygon points="0,0 22,18 313,18 313,95 291,77 0,77" fill="var(--band-grey)"/>
    </svg>
    <div class="person">
      <div class="person-name">GERGELY HALMINDO</div>
      <div class="person-title">MANAGING DIRECTOR</div>
    </div>
    <div class="contact">
      <div class="email">g.halmindo@braskpartnera.hu</div>
      <div class="web">www.braskpartnera.hu</div>
      <div class="address">Brask and Partners Ltd., 1047 Budapest<br>Ravaszi str. 17/B, Hungary</div>
    </div>
  </section>

  <section class="card card-back">
    <div class="card-frame"></div>
    <div class="brand-name"><span class="brand-square"></span>Brask &amp; Partners</div>
  </section>
</body>
</html>
```